Responsive OnePage Design for recruitment company

BrightCrew is a modern company that sources interim people for its customers. Mostly developers, scrum master, project managers and designers. In this website we want to tell something about us, about how we work, our customers and we want our candidates be able to subscribe. The subscription form should be several fields (name, surname, email address, phone number and the possibility to upload your resume.We want it to fit into a existing wordpress plugin. We also want a listing of our job opportunities. The listing should be designed in a clear readable overview and if you click on the job you should get the details and be able to respond quickly by filling in you name, surname, email address, rate, phone number and upload your resume. We want this to be a standard configurable plugin. It should be easy to fill in the jobs in Wordpress by our administrator. We want a fresh, modern and cool design. It should be a responsive onepage design. If you click on a listed job you should stay on the same page. Our logo is added.

Target Market(s)

recruitment

Industry/Entity Type

Recruitment

Font styles to use
Sans Serif

Colors

Designer to choose colors to be used in the design.

Requirements
Must have
• Onepage design
• listing of job opportunities
• subscription forms
• be responsive

```html
<!DOCTYPE html>
<html lang="en">
<head>
<meta charset="utf-8">
<title>BrightCrew – Interim Recruitment</title>
<link href="https://fonts.googleapis.com/css2?family=Dosis:wght@400;500;600&family=Roboto:wght@400;500&display=swap" rel="stylesheet">
<style>
:root{
  --page:#f2e4e4;
  --ink:#222;
  --muted:#555;
  --blue:#1a6fae;
  --red:#e53232;
  --red-soft:#ef9a9a;
  --field:#ececec;
  --white:#fff;
  --hero-a:#0f5c9e;
  --hero-b:#4fb4ea;
  --band-a:#7ee3f6;
  --band-b:#3fb7e0;
}
*{box-sizing:border-box;margin:0;padding:0}
html,body{width:682px;height:1200px;overflow:hidden}
body{background:var(--page);font-family:'Roboto',Arial,sans-serif;color:var(--ink);position:relative}
.abs{position:absolute}

.site-header{left:0;top:0;width:682px;height:54px;border-bottom:1px solid #bbb;border-right:1px solid #222}
.brand{left:14px;top:8px;font:600 10px 'Roboto',sans-serif;color:var(--blue)}
.main-nav{top:8px;left:244px;display:flex;gap:17px;font:400 10px 'Dosis',sans-serif;letter-spacing:.3px}
.main-nav .active{color:#bbb}
.main-nav .signin{background:var(--blue);color:#0c3a5e;padding:1px 3px;border:1px solid #0c3a5e;margin-right:-10px}
.social{left:275px;top:33px;display:flex;gap:11.5px}
.social span{width:12px;height:12px;border-radius:50%;background:var(--red);display:block}

.hero-strip{left:0;top:54px;width:12px;height:221px;background:#d6d6d6}
.hero{left:12px;top:54px;width:655px;height:221px;background:linear-gradient(100deg,var(--hero-a),var(--hero-b) 55%,#2a86c9);text-align:center;color:var(--white)}
.hero h1{font:500 21px 'Dosis',sans-serif;margin-top:65px}
.hero p{font:400 13px/22px 'Dosis',sans-serif;margin-top:8px}

.info-card{top:300px;width:181px;height:97px;background:var(--white);box-shadow:1px 2px 3px rgba(0,0,0,.3);padding:8px 10px}
.info-card h2{font:500 9px 'Roboto',sans-serif;display:flex;align-items:center;gap:4px;white-space:nowrap}
.info-card h2::before,.info-card h2::after{content:"";flex:1;height:1px;background:var(--ink)}
.info-card p{font:400 6.5px/9px 'Roboto',sans-serif;text-align:center;margin-top:6px}
.info-card a{position:absolute;left:11px;bottom:12px;font:400 8px 'Roboto',sans-serif;color:var(--red);text-decoration:none}

.jobs-toggle{left:269px;top:420px;width:145px;height:26px;background:var(--white);border:1px solid #444;border-radius:2px;font:500 9px 'Roboto',sans-serif;display:flex;align-items:center;padding-left:24px}
.jobs-toggle .caret{position:absolute;right:-1px;top:-1px;width:14px;height:26px;background:var(--red);border:1px solid #444}
.jobs-toggle .caret svg{position:absolute;left:3px;top:10px}

.job-board{left:24px;top:468px;width:632px;height:398px;border:1px solid #333;border-radius:3px}
.job-row{left:37px;width:605px;height:80px;border:1px solid #333;border-radius:10px;overflow:hidden;background:var(--page)}
.job-row .num{position:absolute;left:0;top:0;width:37px;height:100%;background:var(--blue);font:400 8px 'Roboto',sans-serif;color:#0c2f50;padding:38px 0 0 16px;border-right:1px solid #333}
.job-row .lbl{position:absolute;top:14px;font:500 8.5px 'Roboto',sans-serif;color:#333}
.job-row .details{position:absolute;left:83px;top:31px;width:136px;height:38px;border:1px solid var(--red);background:var(--white);font:500 8.5px 'Roboto',sans-serif;display:flex;align-items:center;justify-content:center}
.job-row .apply{position:absolute;left:385px;top:29px;width:138px;height:37px;background:var(--red);border:1px solid #333;font:400 8.5px 'Roboto',sans-serif;color:#7a1010;display:flex;align-items:center;justify-content:center}
.job-row .apply.hover{background:var(--red-soft);color:#f7caca;border-color:#aaa}

.apply-panel{left:484px;top:637px;width:162px;height:180px;background:var(--white);box-shadow:0 0 3px rgba(0,0,0,.25);padding:0 11px}
.apply-panel h3,.signup h3{font:500 16px 'Dosis',sans-serif;color:var(--red);text-align:center;margin:14px 0 9px}
.field{height:22px;background:var(--field);border-radius:2px;font:400 7.5px 'Dosis',sans-serif;color:#444;padding:7px 8px;margin-bottom:8px}
.btn-red{height:27px;background:var(--red);color:var(--white);font:500 9.5px 'Dosis',sans-serif;display:flex;align-items:center;justify-content:center;border-radius:2px;letter-spacing:.3px}

.load-more{left:173px;top:830px;width:221px;height:25px;border:1px solid #333;border-bottom:none;border-radius:3px 3px 0 0;font:500 8.5px 'Roboto',sans-serif;display:flex;align-items:center;justify-content:center}

.subscribe-band{left:0;top:889px;width:679px;height:223px;background:linear-gradient(90deg,var(--band-b),var(--band-a) 60%,var(--band-b))}
.subscribe-band h2{position:absolute;left:88px;top:98px;font:500 20px 'Dosis',sans-serif;color:var(--white)}
.subscribe-band svg{position:absolute;left:330px;top:122px}
.signup{left:398px;top:899px;width:162px;height:213px;background:var(--white);box-shadow:0 0 4px rgba(0,0,0,.25);padding:0 11px;border-radius:3px 3px 0 0}
.signup .spacer{height:28px}

.footer-link{top:1130px;font:400 10px 'Dosis',sans-serif;letter-spacing:.3px}
.copyright{left:0;width:682px;top:1173px;text-align:center;font:400 9.5px 'Dosis',sans-serif}
.copyright span{color:var(--blue)}
</style>
</head>
<body>

<header class="site-header abs">
  <div class="brand abs">BrightCrew</div>
  <nav class="main-nav abs">
    <span class="active">HOME</span><span>ABOUT US</span><span>HOW WE WORK</span><span>JOB OPPORTUNITIES ▾</span><span class="signin">SIGN IN</span><span>REGISTER</span>
  </nav>
  <div class="social abs" aria-label="Social links"><span></span><span></span><span></span><span></span><span></span><span></span></div>
</header>

<div class="hero-strip abs"></div>
<section class="hero abs" role="img" aria-label="Photo of business people talking in a meeting, blue tint">
  <h1>We Source Interim People For Our Customers</h1>
  <p>Lorem ipsum dolor sit amet, vis delectus pertinacia ut,<br>ei his clita latine voluptatibus.</p>
</section>

<article class="info-card abs" style="left:32px"><h2>ABOUT US</h2><p>Lorem ipsum dolor sit amet, vis delectus perti-nacia ut, ei his clita latine voluptatibus. No quo constituto scriptorem instructior,quando essent audire vel et.</p><a href="#">READ MORE</a></article>
<article class="info-card abs" style="left:250px"><h2>HOW WE WORK</h2><p>Lorem ipsum dolor sit amet, vis delectus perti-nacia ut, ei his clita latine voluptatibus. No quo constituto scriptorem instructior,quando essent audire vel et.</p><a href="#">READ MORE</a></article>
<article class="info-card abs" style="left:468px"><h2>OUR CUSTOMERS</h2><p>Lorem ipsum dolor sit amet, vis delectus perti-nacia ut, ei his clita latine voluptatibus. No quo constituto scriptorem instructior,quando essent audire vel et.</p><a href="#">READ MORE</a></article>

<div class="jobs-toggle abs">JOB OPPORTUNITIES<span class="caret"><svg width="7" height="5"><path d="M0 0h7L3.5 5z" fill="#0c3a5e"/></svg></span></div>

<section class="job-board abs"></section>

<div class="job-row abs" style="top:480px"><span class="num">1</span><span class="lbl" style="left:53px">Company:</span><span class="lbl" style="left:182px">Position:</span><span class="lbl" style="left:312px">Location:</span><span class="lbl" style="left:495px">Duration:</span><span class="details">Details</span><span class="apply">Apply Now</span></div>
<div class="job-row abs" style="top:566px"><span class="num">2</span><span class="lbl" style="left:53px">Company:</span><span class="lbl" style="left:182px">Position:</span><span class="lbl" style="left:312px">Location:</span><span class="lbl" style="left:495px">Duration:</span><span class="details">Details</span><span class="apply hover">Apply Now</span></div>
<div class="job-row abs" style="top:652px"><span class="num">3</span><span class="lbl" style="left:53px">Company:</span><span class="lbl" style="left:182px">Position:</span><span class="lbl" style="left:312px">Location:</span><span class="details">Details</span><span class="apply">Apply Now</span></div>
<div class="job-row abs" style="top:739px"><span class="num">4</span><span class="lbl" style="left:53px">Company:</span><span class="lbl" style="left:182px">Position:</span><span class="lbl" style="left:312px">Location:</span><span class="details">Details</span><span class="apply">Apply Now</span></div>

<aside class="apply-panel abs">
  <h3>Apply Now!</h3>
  <div class="field">Name</div><div class="field">Surname</div><div class="field">Email</div>
  <div class="btn-red">UPLOAD RESUME</div>
</aside>

<div class="load-more abs">LOAD MORE JOBS</div>

<section class="subscribe-band abs" role="img" aria-label="Group photo of workers from many professions, cyan tint">
  <h2>Subscribe To Our Joblisting</h2>
  <svg width="70" height="30" viewBox="0 0 70 30"><path d="M2 4 Q25 28 62 18" fill="none" stroke="#fff" stroke-width="2.5"/><path d="M55 12 L64 18 L55 23" fill="none" stroke="#fff" stroke-width="2.5"/></svg>
</section>
<aside class="signup abs">
  <h3>Get Started Now!</h3>
  <div class="field">Name</div><div class="field">Phone</div><div class="field">Email</div>
  <div class="spacer"></div>
  <div class="btn-red">UPLOAD RESUME</div>
</aside>

<footer>
  <div class="footer-link abs" style="left:95px">QUICK LINK</div>
  <div class="footer-link abs" style="left:312px;top:1133px">FOLLOW US</div>
  <div class="footer-link abs" style="left:528px;top:1137px">CONTACT US</div>
  <div class="copyright abs">© 2019 Bright<span>Crew</span> All right reserved</div>
</footer>

</body>
</html>
```